Simple HTML Design Needed

We're looking for a simple yet elegant HTML design that will be used for a custom wordpress theme.

We're fairly open to design ideas, but the final product will incorporate elements from the following examples:

http://www.pixomarl.com/widecanvas/
http://layoutbrook.com/demo/tidewell/
http://www.gluvena.at/themedemo/?theme=orbane

We just need the homepage HTML and CSS; we'll create the rest of the pages, unless you want to go above an beyond.

The most creative design will win!

```html
<!DOCTYPE html>
<html lang="en">
<head>
<meta charset="utf-8">
<title>Design Company</title>
<link href="https://fonts.googleapis.com/css2?family=Cabin:wght@400;500&family=Arimo:wght@400;700&display=swap" rel="stylesheet">
<style>
:root{
  --header-dark:#1c1c1c;
  --header-mid:#2a2a2a;
  --page:#e4e4e4;
  --page-light:#eeeeee;
  --nav-home:#473a93;
  --nav-about:#0b8bd2;
  --nav-privacy:#7cc21b;
  --nav-gallery:#f6b900;
  --nav-contact:#f07c10;
  --nav-sitemap:#d7111f;
  --tech-deep:#1b2a44;
  --tech-mid:#2c4468;
  --tech-bar:#15223a;
  --tech-blue:#6cc4f2;
  --tech-link:#4a8bc9;
  --tech-panel:#f1f3f5;
  --motor-red:#9d0d10;
  --motor-dark:#150505;
  --snow-blue:#2a8fd4;
  --snow-sky:#8fd0f2;
  --accent-orange:#e06a10;
  --ink:#555555;
}
*{margin:0;padding:0;box-sizing:border-box}
html,body{width:1200px;height:572px;overflow:hidden}
body{position:relative;background:linear-gradient(var(--page-light),var(--page) 40%);font-family:"Arimo",Arial,sans-serif}

.site-header{position:absolute;left:0;top:0;width:1200px;height:84px;background:linear-gradient(var(--header-mid),var(--header-dark))}
.brand{position:absolute;left:50px;top:20px;display:flex;align-items:center;gap:14px;font-family:"Cabin",sans-serif;font-size:40px;color:#ececec;line-height:1}
.brand-mark{width:48px;height:48px;border-radius:50%;background:#8a8a8a}
.main-nav{position:absolute;left:466px;top:6px;display:flex;list-style:none}
.main-nav li{width:118px;height:78px;display:flex;align-items:flex-start;justify-content:center;padding-top:24px;font-family:"Cabin",sans-serif;font-size:27px;color:#fff}
.main-nav .home{background:var(--nav-home);height:83px}
.main-nav .about{background:var(--nav-about)}
.main-nav .privacy{background:var(--nav-privacy)}
.main-nav .gallery{background:var(--nav-gallery)}
.main-nav .contact{background:var(--nav-contact)}
.main-nav .sitemap{background:var(--nav-sitemap)}

.showcase{position:absolute;left:0;top:84px;width:1200px;height:488px}
.showcase-band{position:absolute;left:0;top:183px;width:1200px;height:225px;background:#f4f4f4}
.preview{position:absolute;overflow:hidden;box-shadow:0 0 8px rgba(0,0,0,.35)}

.preview-far-left{left:0;top:183px;width:26px;height:225px;background:#fff}
.preview-far-left .strip{position:absolute;left:0;top:24px;width:26px;height:90px;background:linear-gradient(#6d8f2a,#a6c64c)}
.preview-far-right{left:1150px;top:183px;width:30px;height:225px;background:#fff}
.preview-far-right .strip{position:absolute;left:0;top:0;width:30px;height:24px;background:#222}
.preview-far-right .photo{position:absolute;left:0;top:24px;width:30px;height:90px;background:linear-gradient(#2a7fa8,#7ec4dc)}

/* motor club template (partly hidden behind the tech template) */
.motor{left:23px;top:101px;width:240px;height:390px;background:linear-gradient(var(--motor-red),#6d0608 70%,var(--motor-dark))}
.motor-top{height:20px;background:#0c0c0c}
.motor-crest{position:absolute;left:16px;top:8px;width:140px;height:122px;background:radial-gradient(circle at 50% 45%,#d9d9d9,#5a1a1a 60%,transparent 75%)}
.motor h2{position:absolute;left:28px;top:150px;font-size:14px;line-height:18px;font-weight:400;color:#fff;white-space:nowrap}
.motor .blurb{position:absolute;left:28px;font-size:7px;line-height:9px;color:#e8b0b0;white-space:nowrap}
.motor h3{position:absolute;left:28px;top:268px;font-size:15px;line-height:18px;font-weight:400;color:#fff;white-space:nowrap}
.motor-article{position:absolute;left:28px;width:200px;display:flex;gap:6px}
.motor-article .thumb{width:22px;height:22px;background:#5a0a0a;flex:none}
.motor-article b{display:block;font-size:7.5px;line-height:10px;color:#fff;white-space:nowrap}
.motor-article span{display:block;font-size:6.5px;line-height:8px;color:#e0a0a0;white-space:nowrap}

/* snow template */
.snow{left:961px;top:101px;width:194px;height:390px;background:#fff}
.snow-top{height:26px;background:#111;color:#ddd;font-size:8px;padding:9px 0 0 0}
.snow-scene{height:214px;background:linear-gradient(var(--snow-sky),var(--snow-blue) 70%,#0c2f5a)}
.snow h2{position:absolute;left:0;top:268px;font-size:19px;color:var(--snow-blue)}
.snow p{position:absolute;left:0;font-size:7.5px;line-height:11px;color:#666;width:190px;white-space:nowrap}
.snow a{color:var(--accent-orange)}

/* tech template */
.tech{left:209px;top:51px;width:760px;height:440px;background:#fff;border:3px solid #d8d8d8;border-bottom:0;z-index:2}
.tech-head{position:absolute;left:0;top:0;width:754px;height:326px;background:radial-gradient(ellipse at 70% 40%,var(--tech-mid),var(--tech-deep) 70%)}
.tech-brand{position:absolute;left:61px;top:16px;display:flex;align-items:center;gap:10px;font-family:"Cabin",sans-serif;font-size:26px;color:#fff;letter-spacing:.5px}
.tech-brand .dot{width:38px;height:38px;border-radius:50%;background:#fff}
.tech-icons{position:absolute;left:612px;top:30px;display:flex;gap:36px}
.tech-nav{position:absolute;left:30px;top:72px;width:724px;height:31px;background:var(--tech-bar);list-style:none}
.tech-nav li{position:absolute;top:9px;font-size:12.5px;color:#c8d6e8;white-space:nowrap}
.tech-nav li:first-child{color:#fff}
.tech-robot{position:absolute;left:295px;top:29px;width:434px;height:293px;background:radial-gradient(ellipse at 50% 55%,#c9cfd6,#6a7a90 45%,transparent 70%)}
.tech-title{position:absolute;left:59px;top:139px;font-family:"Cabin",sans-serif;font-size:18px;color:var(--tech-blue);white-space:nowrap}
.tech-title span{color:#fff}
.tech-lead{position:absolute;left:59px;top:168px;width:290px;font-size:12px;line-height:16.4px;color:#e4ecf5}
.tech-search{position:absolute;left:59px;top:264px;display:flex;gap:7px}
.tech-search .field{width:131px;height:17px;background:#fff}
.tech-search .button{width:63px;height:17px;background:linear-gradient(#cdefff,#7cc8ef);font-size:10.5px;color:#1c4a70;text-align:center;line-height:17px}
.tech-side{position:absolute;left:30px;top:326px;width:218px;height:120px;background:var(--tech-panel)}
.tech-side h2,.tech-main h2{font-family:"Cabin",sans-serif;font-weight:400;color:var(--tech-link);white-space:nowrap}
.tech-side h2{position:absolute;left:20px;top:22px;font-size:21px}
.tech-side .date{position:absolute;left:20px;top:65px;font-size:10px;font-weight:700;color:var(--tech-link)}
.tech-side p{position:absolute;left:20px;top:83px;font-size:12px;color:var(--ink);white-space:nowrap}
.tech-main h2{position:absolute;left:279px;top:348px;font-size:22px}
.tech-main p{position:absolute;left:279px;top:402px;width:415px;font-size:12px;line-height:17px;color:var(--ink)}
</style>
</head>
<body>
<header class="site-header">
  <div class="brand"><span class="brand-mark"></span>Design Company</div>
  <ul class="main-nav">
    <li class="home">Home</li>
    <li class="about">About</li>
    <li class="privacy">Privacy</li>
    <li class="gallery">Gallery</li>
    <li class="contact">Contact</li>
    <li class="sitemap">Sitemap</li>
  </ul>
</header>

<main class="showcase">
  <div class="showcase-band"></div>

  <div class="preview preview-far-left"><div class="strip" role="img" aria-label="Product photo in green tones"></div></div>
  <div class="preview preview-far-right"><div class="strip"></div><div class="photo" role="img" aria-label="Photo in blue tones"></div></div>

  <section class="preview motor">
    <div class="motor-top"></div>
    <div class="motor-crest" role="img" aria-label="Winged skull crest illustration"></div>
    <h2>Welome to Our Motor Club</h2>
    <p class="blurb" style="top:178px">Motor is a free website template created by Team</p>
    <p class="blurb" style="top:198px">The website template goes with two packages - with</p>
    <p class="blurb" style="top:207px">com. The basic package (without PSD is available</p>
    <p class="blurb" style="top:222px">This website template has several pages: Home, About</p>
    <h3>Recent Articles</h3>
    <div class="motor-article" style="top:296px"><span class="thumb" role="img" aria-label="Bike icon"></span><div><b>All About Bikes</b><span>Here you will read about all types of bikes</span></div></div>
    <div class="motor-article" style="top:330px"><span class="thumb" role="img" aria-label="Bike icon"></span><div><b>About Motor Template</b><span>Free 1024x768 Optimized Website Template</span></div></div>
    <div class="motor-article" style="top:364px"><span class="thumb" role="img" aria-label="Bike icon"></span><div><b>Popular Motorcycle Clubs</b></div></div>
  </section>

  <section class="preview snow">
    <div class="snow-top">AP</div>
    <div class="snow-scene" role="img" aria-label="Snowboarder jumping against a blue sky"></div>
    <h2>WORLD!</h2>
    <p style="top:292px">ource.com team. This website template is optimized</p>
    <p style="top:325px">ource files and without them. PSD source files are<br>The basic package (without PSD is available for</p>
    <p style="top:368px"><a>rticle</a> (with Article page), <a>Contact us</a> (note that</p>
  </section>

  <section class="preview tech">
    <div class="tech-head">
      <div class="tech-robot" role="img" aria-label="Crouching white robot illustration"></div>
      <div class="tech-brand"><span class="dot"></span>HIGH TECHNOLOGIES</div>
      <div class="tech-icons">
        <svg width="10" height="10" viewBox="0 0 10 10"><path d="M1 5L5 1L9 5V9H1Z" fill="#fff"/></svg>
        <svg width="10" height="8" viewBox="0 0 10 8"><rect x="0.5" y="0.5" width="9" height="7" fill="none" stroke="#fff"/><path d="M0.5 0.5L5 4.5L9.5 0.5" fill="none" stroke="#fff"/></svg>
        <svg width="10" height="9" viewBox="0 0 10 9"><rect x="1" y="1" width="3" height="3" fill="#fff"/><rect x="6" y="1" width="3" height="3" fill="#fff"/><rect x="1" y="5" width="8" height="3" fill="#fff"/></svg>
      </div>
      <ul class="tech-nav">
        <li style="left:30px">HOME</li>
        <li style="left:97px">ABOUT</li>
        <li style="left:167px">SERVICES</li>
        <li style="left:250px">SUPPORT</li>
        <li style="left:332px">COTACTS</li>
      </ul>
      <h1 class="tech-title"><span>TECHNOLOGIES</span> ARE ALL AROUND US!</h1>
      <p class="tech-lead">Lorem ipsum dolor sit amet, consectetur adipisicing elit, sed do eiusmod tempor incididunt ut labore et dolore magna aliqua. Ut enim ad minim veniam, quis nostrud exercitation ullamco laboris nisi ut aliquip.</p>
      <div class="tech-search"><span class="field"></span><span class="button">SEARCH</span></div>
    </div>
    <aside class="tech-side">
      <h2>Latest News</h2>
      <span class="date">February 15, 2010</span>
      <p>Sed ut perspiciatis unde omnis</p>
    </aside>
    <div class="tech-main">
      <h2>Welcome to High Technologies!</h2>
      <p>High Technologies Site is a free websites template created by Layoutsmith.com team. This website template is optimized for 1024X768 screen resolution. It is also XHTML &amp; CSS valid.</p>
    </div>
  </section>
</main>
</body>
</html>
```